Pine Arbor Table & Chair Rentals

We need a business card for a table and chair rental company. We rent tables and chairs for weddings, funerals, business events and parties. We want something that looks clean and elegant while not being too busy. We would like colors in the green and blue hues and avoiding anything orange. We want to make sure the font is large enough to be seen easily.

Target Market(s)

Wedding & Event Rentals

Industry/Entity Type

Events

Contact Information for Business Card

Pine Arbor, sales@pinearborrentals.example, pinearborrentals.example, 555-218-0937

Requirements
Must have
• Easy to read font
Should not have
• Orange anywhere in the design

```html
<!DOCTYPE html>
<html lang="en">
<head>
<meta charset="utf-8">
<title>Pine Arbor Table &amp; Chair Rentals – Business Card</title>
<link rel="stylesheet" href="https://fonts.googleapis.com/css2?family=Arimo:wght@400&display=swap">
<style>
  :root {
    --page: #ffffff;
    --navy: #0e2846;
    --navy-soft: #2a3f5c;
    --chair-grey: #6f7a8e;
    --ink-light: #ffffff;
  }
  * { margin: 0; padding: 0; box-sizing: border-box; }
  html, body {
    width: 1200px;
    height: 340px;
    overflow: hidden;
    background: var(--page);
  }
  .sheet {
    position: relative;
    width: 1200px;
    height: 340px;
  }
  .card {
    position: absolute;
    top: 11px;
    width: 582px;
    height: 322px;
    background: var(--navy);
    overflow: hidden;
    color: var(--ink-light);
    font-family: "Arimo", Arial, sans-serif;
  }
  .card--front { left: 0; }
  .card--back { left: 618px; }

  .scene-art {
    position: absolute;
    inset: 0;
    background:
      linear-gradient(90deg,
        var(--chair-grey) 0%,
        var(--navy-soft) 16%,
        var(--navy) 32%,
        var(--navy) 68%,
        var(--navy-soft) 84%,
        var(--chair-grey) 100%);
  }

  .brand-name {
    position: absolute;
    left: 0;
    width: 100%;
    text-align: center;
    font-weight: 400;
    letter-spacing: 1px;
    line-height: 1;
  }
  .card--front .brand-name {
    top: 133px;
    font-size: 40px;
  }
  .card--back .brand-name {
    top: 88px;
    font-size: 38px;
  }

  .divider {
    position: absolute;
    left: 134px;
    top: 153px;
  }

  .contact {
    position: absolute;
    top: 176px;
    left: 0;
    width: 100%;
    list-style: none;
    text-align: center;
    font-size: 20px;
    line-height: 28px;
  }
</style>
</head>
<body>
  <main class="sheet">
    <section class="card card--front" aria-label="Card front">
      <div class="scene-art" role="img" aria-label="Two chairs facing each other across a dashed aisle"></div>
      <h1 class="brand-name">Pine Arbor</h1>
    </section>

    <section class="card card--back" aria-label="Card back">
      <h2 class="brand-name">Pine Arbor</h2>
      <svg class="divider" width="314" height="14" viewBox="0 0 314 14" aria-hidden="true">
        <line x1="0" y1="7" x2="302" y2="7" stroke="var(--ink-light)" stroke-width="1.5"/>
        <polygon points="302,2 314,7 302,12" fill="var(--ink-light)"/>
      </svg>
      <ul class="contact">
        <li class="contact__email">sales@pinearborrentals.example</li>
        <li class="contact__web">pinearborrentals.example</li>
        <li class="contact__phone">555-218-0937</li>
      </ul>
    </section>
  </main>
</body>
</html>
```